Letterhead for a German Distribution/Manufacturing Company

We need a professional Letterhead in a unique Design.
not to playful.
The Letterhead has to show show that we are a international company with headquater in Germany.
all details like adress, Vat Tax Number, Bank Accout, Eori, email, Company number has to be on the Letterhead.
for example use: VAT TAX DE5704168 Bank Account: Norrfeld Bank IBAN DE421705238ß310482 Swift: KOLV3154802 EORI 3041296587 Company Number: HRB 61508 Adress: VOLTRINA UG Amsel Strasse 7 Postal Code 04683 City Feldbrunn Country: Germany Email: info@voltrina-example.com
the design can be colored but doesnt have to be
Industry/Entity Type
Manufacturing and international distribution
Requirements
Must have
- show that we are a international company with headquater in Germany. our company infos and logo

```html
<!DOCTYPE html>
<html lang="en">
<head>
<meta charset="utf-8">
<title>Voltrina UG Letterhead</title>
<link href="https://fonts.googleapis.com/css2?family=Roboto:wght@300;400;500;700&display=swap" rel="stylesheet">
<style>
  :root {
    --backdrop: #e6e6e6;
    --paper: #f1f1f1;
    --band-dark: #454545;
    --band-light: #d6d6d6;
    --ink: #2b2b2b;
    --ink-soft: #5a5a5a;
    --accent: #1f4f9c;
    --white: #ffffff;
  }
  * { box-sizing: border-box; margin: 0; padding: 0; }
  html, body { width: 1200px; height: 794px; overflow: hidden; }
  body {
    background: var(--backdrop);
    font-family: 'Roboto', sans-serif;
    color: var(--ink);
    display: flex; align-items: center; justify-content: center;
  }
  .letterhead {
    position: relative;
    width: 540px; height: 764px;
    background: var(--paper);
    box-shadow: 0 2px 8px rgba(0,0,0,.12);
  }
  .header-band {
    height: 84px;
    background: var(--band-dark);
    display: flex; align-items: center;
    padding: 0 30px;
    color: var(--white);
  }
  .brand { display: flex; align-items: center; gap: 8px; flex: 1; }
  .brand-mark { width: 16px; height: 16px; border-radius: 50%; background: var(--white); }
  .brand-name { font-size: 19px; font-weight: 400; letter-spacing: 1px; }
  .header-divider { width: 1px; height: 52px; background: #8a8a8a; margin-right: 16px; }
  .contact-list { list-style: none; font-size: 7.5px; font-weight: 300; line-height: 1.35; }
  .contact-list li { display: flex; align-items: flex-start; gap: 7px; margin: 3px 0; }
  .contact-icon { width: 10px; height: 10px; flex: none; background: var(--white); border-radius: 1px; display: flex; align-items: center; justify-content: center; }
  .sub-band { height: 18px; background: var(--band-light); margin-left: 255px; }
  .company-details {
    display: flex; gap: 28px;
    padding: 14px 30px 0;
    font-size: 7.5px; line-height: 1.6; color: var(--ink-soft);
  }
  .company-details strong { color: var(--ink); font-weight: 700; }
  .letter-date { position: absolute; top: 132px; right: 34px; font-size: 7.5px; color: var(--ink-soft); }
  .recipient { padding: 34px 30px 0 74px; font-size: 7.5px; line-height: 1.6; color: var(--ink-soft); }
  .recipient-name { font-size: 9.5px; font-weight: 700; color: var(--ink); }
  .recipient-name span { color: var(--accent); }
  .recipient b { color: var(--accent); }
  .letter-body { padding: 22px 34px 0 74px; font-size: 7.8px; line-height: 1.65; color: var(--ink-soft); }
  .letter-body p { margin-bottom: 14px; }
  .signature { padding: 14px 0 0 272px; font-size: 8px; line-height: 1.4; }
  .signature-mark { width: 70px; height: 20px; background: linear-gradient(90deg, #d9d9d9, #c9c9c9); margin-bottom: 3px; }
  .signer-name { font-weight: 700; }
  .footer-tab { position: absolute; bottom: 0; left: 400px; width: 56px; height: 22px; background: var(--band-dark); }
</style>
</head>
<body>
<main class="letterhead">
  <header>
    <div class="header-band">
      <div class="brand">
        <span class="brand-mark"></span>
        <span class="brand-name">VOLTRINA</span>
      </div>
      <span class="header-divider"></span>
      <ul class="contact-list">
        <li><span class="contact-icon"><svg width="7" height="7" viewBox="0 0 10 10"><path d="M2 1l2 2-1 1.5c.8 1.4 1.6 2.2 3 3L7.5 6l2 2-1.5 1.5C4.5 9 1 5.5.5 2.5z" fill="#454545"/></svg></span>+49 3724 58 210</li>
        <li><span class="contact-icon"><svg width="7" height="6" viewBox="0 0 10 8"><rect x=".5" y=".5" width="9" height="7" fill="none" stroke="#454545"/><path d="M.5 .5l4.5 4 4.5-4" fill="none" stroke="#454545"/></svg></span>info@voltrina-example.com</li>
        <li><span class="contact-icon"><svg width="6" height="8" viewBox="0 0 8 10"><path d="M4 0a3.5 3.5 0 0 0-3.5 3.5C.5 6 4 10 4 10s3.5-4 3.5-6.5A3.5 3.5 0 0 0 4 0z" fill="#454545"/></svg></span>VOLTRINA UG, Amsel Strasse 7<br>04683 Feldbrunn, Germany</li>
      </ul>
    </div>
    <div class="sub-band"></div>
    <div class="company-details">
      <div><strong>Vat Tax:</strong> DE5704168<br><strong>Company Number:</strong> HRB 61508</div>
      <div><strong>Bank Account:</strong> Norrfeld Bank IBAN DE421705238ß310482<br><strong>Swift:</strong> KOLV3154802 EORI 3041296587</div>
    </div>
  </header>

  <p class="letter-date">Date: 25 September, 2022</p>

  <section class="recipient">
    <p class="recipient-name">Lena <span>Hartwig</span></p>
    <p>Designer</p>
    <p><b>A :</b> Lindenau City, Zip Code : 215</p>
    <p><b>W :</b> www.lenahartwig-example.com</p>
    <p><b>P :</b> +49 371 846 229</p>
  </section>

  <section class="letter-body">
    <p>Lorem ipsum dolor sit amet, consectetur adipisicing elit, sed do eiusmod tempor incididunt ut labore et dolore magna aliqua. Ut enim ad minim veniam, quis nostrud exercitation ullamco laboris nisi ut aliquip ex ea commodo consequat.</p>
    <p>Excepteur sint occaecat cupidatat non proident, sunt in culpa qui officia deserunt mollit anim id est laborum. Sed ut perspiciatis unde omnis iste natus error sit voluptatem accusantium doloremque laudantium, totam rem aperiam, eaque ipsa quae ab illo inventore veritatis et quasi architecto beatae vitae dicta sunt explicabo. Nemo enim ipsam voluptatem quia voluptas sit aspernatur aut odit aut fugit, sed quia consequuntur magni dolores eos qui ratione voluptatem sequi nesciunt. Sunt in culpa qui officia iste natus error sit voluptatem accusantium doloremque laudantium.</p>
    <p>Totam rem aperiam, eaque ipsa quae ab illo inventore veritatis et quasi architecto beatae vitae dicta sunt explicabo. Nemo enim ipsam voluptatem quia voluptas sit aspernatur aut odit aut fugit, sed quia consequuntur magni dolores eos qui ratione voluptatem sequi nesciunt.</p>
    <p>Neque porro quisquam dolorem ipsum quia dolor sit amet, consectetur adipisci velit, sed quia non numquam eius modi tempora incidunt ut labore et dolore magnam aliquam quaerat voluptatem.</p>
  </section>

  <section class="signature">
    <div class="signature-mark" role="img" aria-label="Handwritten signature of Markus Feld"></div>
    <p class="signer-name">Markus Feld</p>
    <p>Manager</p>
  </section>

  <div class="footer-tab"></div>
</main>
</body>
</html>
```